Business Card Design Needed

Business car design required, logo will be supplied.

Brambleford Power Surveyors are looking to become the leading provider of energy performance certificates to estate agents, landlords and home owners in the Yorkshire region of the UK.

The business card must be double sided and professional looking. Estate agents receive hundreds of cards from contractors and our card must stand out.

I require a two sided business card that is clean, modern and created by a designer that can think outside of the box.

Brand colours can be supplied .

Please ask if you have any questions.

Target Market(s)

Estate agents, landlords and property owners

Industry/Entity Type

Property - estate agency - energy consultants

Contact Information for Business Card

Tomas Rendell - Energy Assessor - 07311642705 - www.BramblefordPSV.co.uk - info@bramblefordpsv.co.uk

Font styles to use
Serif
Sans Serif

Colors
00AB8E
00BBA5
67D7C9
C6EFE9
E9F9F6

Requirements
Must have
• Use the provided logo, clean, professional and stand out from the crowd
Nice to have
• Clever use of text, spacing and brand colours
Should not have
• Clip art

```html
<!DOCTYPE html>
<html lang="en">
<head>
<meta charset="utf-8">
<title>Brambleford Power Surveyors – Business Card</title>
<link href="https://fonts.googleapis.com/css2?family=Montserrat:wght@300;400;500;700&display=swap" rel="stylesheet">
<style>
  :root {
    --stage: #1c1d1f;
    --card-white: #f7f7f5;
    --brand-blue: #0d5fa6;
    --brand-blue-light: #1aa3e0;
    --brand-blue-deep: #0a3f86;
    --lime: #b5d334;
    --charcoal: #3a3c3f;
    --text-light: #f2f2f2;
  }
  * { margin: 0; padding: 0; box-sizing: border-box; }
  html, body {
    width: 1200px; height: 874px; overflow: hidden;
    background: var(--stage);
    font-family: "Montserrat", sans-serif;
  }
  .canvas { position: relative; width: 1200px; height: 874px; }

  .card {
    position: absolute;
    width: 560px; height: 320px;
    border-radius: 18px;
    overflow: hidden;
    box-shadow: 0 12px 30px rgba(0,0,0,0.55);
  }

  /* Back side */
  .card-back { left: 520px; top: 70px; }
  .card-back .pattern-fill {
    position: absolute; inset: 0;
    background: linear-gradient(120deg, var(--brand-blue-light) 0%, var(--brand-blue) 50%, var(--brand-blue-deep) 100%);
  }

  /* Front side */
  .card-front { left: 140px; top: 470px; background: var(--card-white); }
  .card-front .wave { position: absolute; inset: 0; width: 100%; height: 100%; }

  .brand {
    position: absolute; left: 52px; top: 52px;
    display: flex; align-items: center; gap: 14px;
  }
  .brand-dot {
    width: 40px; height: 40px; border-radius: 50%;
    background: var(--brand-blue);
    flex: none;
  }
  .brand-name {
    color: var(--brand-blue);
    font-weight: 400;
    font-size: 22px;
    letter-spacing: 1px;
    line-height: 1.15;
    text-transform: uppercase;
  }

  .contact {
    position: absolute; right: 28px; top: 198px;
    text-align: right;
    color: var(--text-light);
  }
  .contact-name {
    color: var(--lime);
    font-weight: 700;
    font-size: 19px;
    line-height: 24px;
    letter-spacing: 0.5px;
    text-transform: uppercase;
  }
  .contact-role {
    font-size: 12.5px; font-weight: 400;
    line-height: 17px;
    margin-bottom: 7px;
  }
  .contact-line {
    display: flex; justify-content: flex-end; align-items: center; gap: 8px;
    font-size: 12px; line-height: 19px; font-weight: 400;
  }
  .contact-line svg { width: 11px; height: 11px; fill: var(--lime); flex: none; }
</style>
</head>
<body>
<div class="canvas">

  <section class="card card-back">
    <div class="pattern-fill" role="img" aria-label="Embossed repeating pattern of the company mark on a blue gradient"></div>
  </section>

  <section class="card card-front">
    <svg class="wave" viewBox="0 0 560 320" preserveAspectRatio="none" aria-hidden="true">
      <path d="M0,122 C110,190 240,206 340,194 C430,182 500,156 560,128 L560,320 L0,320 Z" fill="var(--charcoal)"/>
      <path d="M0,112 C110,180 240,196 340,184 C430,172 500,146 560,118" fill="none" stroke="var(--brand-blue)" stroke-width="9"/>
      <path d="M50,174 C160,200 270,202 350,190 C430,178 500,152 560,134" fill="none" stroke="var(--lime)" stroke-width="7"/>
    </svg>

    <div class="brand">
      <span class="brand-dot"></span>
      <span class="brand-name">Brambleford<br>Power Surveyors</span>
    </div>

    <div class="contact">
      <p class="contact-name">Tomas Rendell</p>
      <p class="contact-role">Energy Assessor</p>
      <p class="contact-line">07311642705
        <svg viewBox="0 0 24 24"><path d="M6.6 10.8a15.1 15.1 0 0 0 6.6 6.6l2.2-2.2a1 1 0 0 1 1-.25 11.4 11.4 0 0 0 3.6.57 1 1 0 0 1 1 1V20a1 1 0 0 1-1 1A17 17 0 0 1 3 4a1 1 0 0 1 1-1h3.5a1 1 0 0 1 1 1c0 1.250.2 2.45.57 3.57a1 1 0 0 1-.25 1z"/></svg>
      </p>
      <p class="contact-line">info@bramblefordpsv.co.uk
        <svg viewBox="0 0 24 24"><path d="M2 5h20v14H2z M4 7v.5l8 5 8-5V7z" fill-rule="evenodd"/></svg>
      </p>
      <p class="contact-line">www.BramblefordPSV.co.uk
        <svg viewBox="0 0 24 24"><path d="M12 2a10 10 0 1 0 0 20 10 10 0 0 0 0-20zm0 2c1.2 0 2.6 2.3 3 6H9c.4-3.7 1.8-6 3-6zm-7.8 6A8 8 0 0 1 8 4.9 14 14 0 0 0 7 10zm0 4H7a14 14 0 0 0 1 5.1A8 8 0 0 1 4.2 14zM12 20c-1.2 0-2.6-2.3-3-6h6c-.4 3.7-1.8 6-3 6zm4-.9a14 14 0 0 0 1-5.1h2.8a8 8 0 0 1-3.8 5.1zM17 10a14 14 0 0 0-1-5.1 8 8 0 0 1 3.8 5.1z"/></svg>
      </p>
    </div>
  </section>

</div>
</body>
</html>
```